Design an Outstanding flyer for my company.

I need a flyer designed for our window tinting company based in Brisbane Queensland Australia. The flyer will be targeting Home tinting. We also do mobile car tinting. Something in regards to this could be incorporated into the flyer as well.
I want it to be 2 sided DL size. Black background.
It really needs to Pop, and be a real attention getter.
It needs to be easy to read.
I have provided a mock up with the info on it from our marketing company. It will need a spellcheck etc to make sure everything is correct.
Everything about it can be changed however you like.
I have also included the company logo.

Lets see what you've got!

Target Market(s)

Home Owners

Industry/Entity Type

Home Improvement

Font styles to use
Other font styles liked:
• Duan Penh

Requirements
Must have
• All the information on the mock up. Clear and easy to read.
• Must Stand Out!

```html
<!DOCTYPE html>
<html lang="en">
<head>
<meta charset="utf-8">
<title>BrightSun Window Tinting – DL Flyer</title>
<link rel="stylesheet" href="https://fonts.googleapis.com/css2?family=Cinzel:wght@400;600&family=Roboto+Condensed:wght@700&family=Arimo:wght@400;700&display=swap">
<style>
  :root{
    --stage-light:#5e5e5e;
    --stage-dark:#333333;
    --ink:#0b0b0b;
    --yellow:#ecdf2a;
    --gold:#e6c417;
    --gold-deep:#c9a20c;
    --gold-light:#f3dc52;
    --white:#ffffff;
    --swoosh:#9b9b9b;
    --serif:"Cinzel", "Times New Roman", serif;
    --condensed:"Roboto Condensed", "Arial Narrow", sans-serif;
    --sans:"Arimo", Arial, sans-serif;
  }
  *{box-sizing:border-box;margin:0;padding:0}
  html,body{width:1200px;height:960px;overflow:hidden}
  body{background:radial-gradient(ellipse at 50% 30%, var(--stage-light), var(--stage-dark) 85%);position:relative;font-family:var(--sans)}

  .flyer{position:absolute;width:440px;height:885px;background:var(--ink);box-shadow:0 0 0 1px #6d6d6d;overflow:hidden;color:var(--white)}
  .flyer--front{left:110px;top:45px}
  .flyer--back{left:628px;top:47px}

  .headline{position:absolute;left:0;width:100%;text-align:center;text-transform:uppercase}
  .headline__line{display:block;white-space:nowrap;line-height:1}
  .headline__heat{font-family:var(--serif);color:var(--gold);font-size:33px;font-weight:400}
  .headline__uv{font-family:var(--serif);font-size:22px;margin-top:12px}
  .headline__money{font-family:var(--condensed);color:var(--gold);font-size:55px;font-weight:700;margin-top:8px;letter-spacing:.5px}
  .headline__privacy{font-family:var(--serif);font-size:27px;margin-top:9px}

  .band{position:absolute;left:0;width:440px;height:300px}
  .band svg{position:absolute;inset:0}
  .band__text{position:absolute;left:37px;width:368px;color:#111;font-size:11.6px;line-height:17.3px;text-align:justify;text-transform:uppercase}

  .reasons{position:absolute;left:32px;width:377px;height:81px;border:1.5px solid #f5e9a0;border-radius:6px;
    background:linear-gradient(180deg,var(--gold-light),var(--gold) 45%,var(--gold-deep));
    display:flex;align-items:center;justify-content:center;text-align:center;
    font-family:var(--sans);font-weight:700;font-size:17px;line-height:23px;color:#111}

  .call{position:absolute;left:0;width:100%;text-align:center;font-family:var(--serif);font-size:19px;line-height:29px;white-space:nowrap;text-transform:uppercase}
  .call__tag{background:var(--yellow);color:#111;border-radius:4px;padding:0 4px}

  .contact{position:absolute;left:0;width:100%;height:60px}
  .contact__divider{position:absolute;left:217px;top:0;width:2px;height:54px;background:var(--gold)}
  .contact__icon{position:absolute;top:0;width:14px;height:12px}
  .contact__number{position:absolute;top:18px;font-size:26px;white-space:nowrap}
  .contact__number--landline{left:48px;font-family:var(--condensed);font-weight:700}
  .contact__number--mobile{left:242px;font-family:var(--sans);font-size:23px;top:20px}

  .web{position:absolute;left:68px;display:flex;align-items:center;gap:16px;font-size:18px;white-space:nowrap}
  .rule{position:absolute;left:25px;width:390px;height:2px;background:linear-gradient(90deg,transparent,var(--gold) 50%,transparent)}

  .brand{position:absolute;left:0;width:100%;display:flex;align-items:center;justify-content:center;gap:12px}
  .brand__dot{width:26px;height:26px;border-radius:50%;background:var(--gold)}
  .brand__name{font-family:var(--serif);font-weight:600;font-size:21px;color:var(--gold);white-space:nowrap;letter-spacing:.5px}

  /* front layout */
  .flyer--front .headline{top:32px}
  .flyer--front .band{top:192px}
  .flyer--front .band__text{top:61px}
  .flyer--front .reasons{top:450px}
  .flyer--front .call{top:560px}
  .flyer--front .contact{top:640px}
  .flyer--front .web{top:716px}
  .flyer--front .rule{top:766px}
  .flyer--front .brand{top:810px}

  /* back layout */
  .flyer--back .reasons{top:35px}
  .flyer--back .headline{top:145px}
  .flyer--back .band{top:313px}
  .flyer--back .band__text{top:62px}
  .flyer--back .call{top:568px}
  .flyer--back .contact{top:642px}
  .flyer--back .web{top:715px}
  .flyer--back .rule{top:767px}
  .flyer--back .brand{top:813px}
</style>
</head>
<body>

<svg width="0" height="0" style="position:absolute" aria-hidden="true">
  <defs>
    <symbol id="icon-phone" viewBox="0 0 14 12"><path d="M1 4 Q7 -1 13 4 L11 5.5 L9.5 3.8 L4.5 3.8 L3 5.5 Z M3.5 6 H10.5 L12 11 H2 Z" fill="#ecdf2a"/><circle cx="7" cy="8.3" r="1.6" fill="#0b0b0b"/></symbol>
    <symbol id="icon-sms" viewBox="0 0 14 12"><rect x="0.5" y="0.5" width="13" height="8.5" rx="2" fill="#ecdf2a"/><path d="M3 9 L3 12 L6.5 9 Z" fill="#ecdf2a"/></symbol>
    <symbol id="band-shape" viewBox="0 0 440 300">
      <path d="M0 22 Q220 60 440 8 L440 215 Q200 215 0 268 Z" fill="#ecdf2a"/>
      <path d="M180 36 Q330 30 440 -4 L440 8 Q330 44 180 36 Z" fill="#9b9b9b"/>
      <path d="M0 268 Q200 215 440 215 Q200 224 0 285 Z" fill="#9b9b9b"/>
    </symbol>
    <symbol id="icon-globe" viewBox="0 0 16 16"><circle cx="8" cy="8" r="7" fill="none" stroke="#ecdf2a" stroke-width="1.4"/><ellipse cx="8" cy="8" rx="3" ry="7" fill="none" stroke="#ecdf2a" stroke-width="1.2"/><path d="M1 8 H15 M2.5 4.5 H13.5 M2.5 11.5 H13.5" stroke="#ecdf2a" stroke-width="1.2"/></symbol>
  </defs>
</svg>

<article class="flyer flyer--front">
  <div class="headline">
    <span class="headline__line headline__heat">Keep Heat Out</span>
    <span class="headline__line headline__uv">Block 99.9% UV Rays</span>
    <span class="headline__line headline__money">SAVE MONEY</span>
    <span class="headline__line headline__privacy">Increase Privacy</span>
  </div>
  <div class="band">
    <svg viewBox="0 0 440 300" aria-hidden="true"><use href="#band-shape"/></svg>
    <p class="band__text">Reduce glare. Reduce energy costs. Control the amount of light entering your home. Reduce carbon footprint. Make home more beautiful. Eliminate home hot spots. Protect against broken glass. Regulate energy. Protects upholstery. Improve effectiveness of roof insulation. Improve health. Reduces interior floor fading. Eliminate need for blinds. Strengthen your windows. Insulate in winter. Affordable.</p>
  </div>
  <div class="reasons">20 REASONS WHY<br>HOME WINDOW TINTING<br>IS PERFECT FOR YOU.</div>
  <p class="call"><span class="call__tag">Call</span> Brisbane’s Leader in<br>Home Window Tinting Now.</p>
  <div class="contact">
    <svg class="contact__icon" style="left:115px" aria-hidden="true"><use href="#icon-phone"/></svg>
    <span class="contact__number contact__number--landline">07 3000 1846</span>
    <span class="contact__divider"></span>
    <svg class="contact__icon" style="left:310px" aria-hidden="true"><use href="#icon-sms"/></svg>
    <span class="contact__number contact__number--mobile">0400 555 018</span>
  </div>
  <p class="web"><svg width="16" height="16" aria-hidden="true"><use href="#icon-globe"/></svg>www.brightsuntinting.com.au</p>
  <div class="rule"></div>
  <div class="brand"><span class="brand__dot"></span><span class="brand__name">BRIGHTSUN WINDOW TINTING</span></div>
</article>

<article class="flyer flyer--back">
  <div class="reasons">20 REASONS WHY<br>HOME WINDOW TINTING<br>IS PERFECT FOR YOU.</div>
  <div class="headline">
    <span class="headline__line headline__heat">Keep Heat Out</span>
    <span class="headline__line headline__uv">Block 99.9% UV Rays</span>
    <span class="headline__line headline__money">SAVE MONEY</span>
    <span class="headline__line headline__privacy">Increase Privacy</span>
  </div>
  <div class="band">
    <svg viewBox="0 0 440 300" aria-hidden="true"><use href="#band-shape"/></svg>
    <p class="band__text">Reduce glare. Reduce energy costs. Control the amount of light entering your home. Reduce carbon footprint. Make home more beautiful. Eliminate home hot spots. Protect against broken glass. Regulate energy. Protects upholstery. Improve effectiveness of roof insulation. Improve health. Reduces interior floor fading. Eliminate need for blinds. Strengthen your windows. Insulate in winter. Affordable.</p>
  </div>
  <p class="call"><span class="call__tag">Call</span> Brisbane’s Leader in<br>Home Window Tinting Now.</p>
  <div class="contact">
    <svg class="contact__icon" style="left:115px" aria-hidden="true"><use href="#icon-phone"/></svg>
    <span class="contact__number contact__number--landline">07 3000 1846</span>
    <span class="contact__divider"></span>
    <svg class="contact__icon" style="left:310px" aria-hidden="true"><use href="#icon-sms"/></svg>
    <span class="contact__number contact__number--mobile">0400 555 018</span>
  </div>
  <p class="web"><svg width="16" height="16" aria-hidden="true"><use href="#icon-globe"/></svg>www.brightsuntinting.com.au</p>
  <div class="rule"></div>
  <div class="brand"><span class="brand__dot"></span><span class="brand__name">BRIGHTSUN WINDOW TINTING</span></div>
</article>

</body>
</html>
```